Corvane Holdings , new business card design

investment firm with corporate clients . need double sided business card , vertical and horizontal options ,logo must be clear. prefer pantone colors only and sharp design. website also www.corvane-demo.ae

Khalid Bin Rashed
Managing Director
Tel. +971 4 000 1234
Mobile +971 50 000 5678
khalid@corvane-demo.ae
Palmgate Tower, officw 18-B07, Noor Terraces, Dubai

Khalid Bin Rashed
Managing Director

Serif

Designer to choose colors to be used in the design.

```html
<!DOCTYPE html>
<html lang="en">
<head>
<meta charset="utf-8">
<title>Corvane Holdings – Business Card</title>
<link rel="stylesheet" href="https://fonts.googleapis.com/css2?family=Mulish:wght@300;400;700&display=swap">
<style>
  :root {
    --backdrop: #e6e3e0;
    --card-white: #f8f8f8;
    --navy: #46455e;
    --accent-blue: #2f6389;
    --name-blue: #3a6d9c;
    --ink: #3c3c48;
    --rule: #9a9aa2;
  }
  html, body {
    margin: 0;
    width: 1200px;
    height: 997px;
    overflow: hidden;
    background: var(--backdrop);
    font-family: "Mulish", sans-serif;
  }
  .sheet {
    position: relative;
    width: 1200px;
    height: 997px;
  }
  .card {
    position: absolute;
    left: 220px;
    width: 760px;
    height: 434px;
    overflow: hidden;
    box-shadow: 0 6px 18px rgba(0,0,0,0.12);
  }
  .card-front { top: 44px; background: var(--card-white); }
  .card-back  { top: 519px; background: var(--navy); }

  .wordmark {
    position: absolute;
    font-weight: 300;
    line-height: 1;
    text-transform: uppercase;
  }
  .wordmark .primary { display: block; font-size: 40px; letter-spacing: 14px; }
  .wordmark .secondary { display: block; font-size: 13px; letter-spacing: 11.6px; margin-top: 8px; }

  .card-front .wordmark { left: 48px; top: 86px; color: var(--navy); }
  .card-back .wordmark {
    left: 50%; top: 50%;
    transform: translate(-50%, -50%);
    color: #ffffff;
  }
  .card-back .wordmark .primary { font-size: 50px; letter-spacing: 18px; }
  .card-back .wordmark .secondary { font-size: 16px; letter-spacing: 14.8px; }

  .divider {
    position: absolute;
    left: 40px;
    top: 180px;
    width: 440px;
    height: 1px;
    background: var(--rule);
  }
  .contact-rule {
    position: absolute;
    left: 40px;
    top: 262px;
    width: 190px;
    height: 1px;
    background: var(--rule);
  }

  .identity {
    position: absolute;
    right: 44px;
    top: 82px;
    text-align: right;
    color: var(--ink);
  }
  .identity .person-name {
    margin: 0;
    font-size: 19px;
    font-weight: 700;
    color: var(--name-blue);
  }
  .identity .person-title {
    margin: 4px 0 0;
    font-size: 14px;
    display: flex;
    align-items: center;
    justify-content: flex-end;
    gap: 4px;
  }
  .identity .person-title::before {
    content: "";
    width: 60px;
    height: 1px;
    background: var(--ink);
  }
  .identity .address {
    margin: 16px 0 0;
    font-size: 14px;
    line-height: 1.55;
    font-style: normal;
  }

  .wave {
    position: absolute;
    left: 0;
    top: 0;
    width: 760px;
    height: 434px;
  }

  .contacts {
    position: absolute;
    left: 52px;
    top: 276px;
    margin: 0;
    padding: 0;
    list-style: none;
    font-size: 16px;
    color: var(--ink);
  }
  .contacts li {
    display: flex;
    align-items: center;
    gap: 9px;
    line-height: 24px;
  }
  .contacts svg { width: 13px; height: 13px; fill: var(--accent-blue); flex: none; }
</style>
</head>
<body>
<main class="sheet">
  <section class="card card-front" aria-label="Business card front">
    <svg class="wave" viewBox="0 0 760 434" aria-hidden="true">
      <path d="M0 434 C 400 430, 600 330, 760 236 L 760 434 Z" fill="var(--accent-blue)"/>
      <path d="M40 434 C 440 428, 620 338, 760 246 L 760 434 Z" fill="#ffffff"/>
      <path d="M120 434 C 480 424, 640 350, 760 260 L 760 434 Z" fill="var(--navy)"/>
    </svg>

    <div class="wordmark">
      <span class="primary">Corvane</span>
      <span class="secondary">Holdings</span>
    </div>

    <div class="divider"></div>

    <div class="identity">
      <h1 class="person-name">Khalid Bin Rashed</h1>
      <p class="person-title">Managing Director</p>
      <address class="address">Palmgate Tower, officw 18-B07,<br>Noor Terraces, Dubai</address>
    </div>

    <div class="contact-rule"></div>

    <ul class="contacts">
      <li>
        <svg viewBox="0 0 16 16" aria-hidden="true"><path d="M3.5 1.5 6 4 4.6 5.6c.8 2.2 3.6 5 5.8 5.8L12 10l2.5 2.5-1.8 2C7.5 14 2 8.5 1.5 3.3z"/></svg>
        <span>+971 50 000 5678</span>
      </li>
      <li>
        <svg viewBox="0 0 16 16" aria-hidden="true"><path d="M4 1h8v14H4zM5.4 2.4v9.6h5.2V2.4z"/></svg>
        <span>+971 50 000 5678</span>
      </li>
      <li>
        <svg viewBox="0 0 16 16" aria-hidden="true"><path d="M1 3h14v10H1zM2 4.2v.4l6 4.2 6-4.2v-.4z"/></svg>
        <span>khalid@corvane-demo.ae</span>
      </li>
    </ul>
  </section>

  <section class="card card-back" aria-label="Business card back">
    <div class="wordmark">
      <span class="primary">Corvane</span>
      <span class="secondary">Holdings</span>
    </div>
  </section>
</main>
</body>
</html>
```